Online-Marketing Material für Recruiting-Plattform
Zielgruppe
Recruiting-Plattform für Physiotherapeuten. Wir sind Vermittler.
Aufgabenstellung
Ich benötige ein 2er Set aus Social-Media-Templates, das wir als Basis für Recruiting-Ads nutzen können.
Variante 1: (1080 x 1350) mit jeweils 285 Pixel Safe Space oben und unten (hier keine wichtigen Elemente).
Wichtig: Es handelt sich um ein Template. Daher muss es mit verschiedenen Elementen und Fotos funktionieren.
Die Elemente werden später durch variable Inhalte gesetzt. Ziel ist es, ein möglichst flexibles Format zu schaffen,
das mit unterschiedlichen Inhalten funktioniert.
Bitte orientiere dich am Grunddesign der Website therapunkt.de
Elemente und zugehörige Beispiele sind
1. Foto in querformat | Beispiel als Download)
2. Jobtitel als Headline | (Physiotherapeut (m/w/d)
3. Subtitle | Werde Teil eines wachsenden Teams
4. Arbeitszeitmodell | Vollzeit, Teilzeit
3. Ort | Hannover
4. 3 x Highlights | 1. Betriebliche Krankenversicherung 2. Tretlux 3. Gehalt bis zu 4.500 EUR
(Die Highlight variieren thematisch, daher hier bitte nur mit thematisch-neutralen Icons arbeiten.
5. Logo des Arbeitgebers (lusen) auf weiß
Variante 2 mit Foto in hochformat

```html
<!DOCTYPE html>
<html lang="de">
<head>
<meta charset="utf-8">
<title>Physiotherapeut (m/w/d) – Stellenanzeige</title>
<link rel="stylesheet" href="https://fonts.googleapis.com/css2?family=Roboto:wght@300;400;700;900&display=swap">
<style>
  :root {
    --deep-teal: #003d4c;
    --brand-teal: #00959e;
    --slate: rgba(52, 98, 112, 0.86);
    --aqua: rgba(38, 170, 178, 0.86);
    --sun: rgba(250, 200, 72, 0.86);
    --white: #ffffff;
  }
  * { margin: 0; padding: 0; box-sizing: border-box; }
  html, body { width: 960px; height: 1200px; overflow: hidden; background: var(--white); }
  body { font-family: "Roboto", Arial, sans-serif; color: var(--white); }
  .ad { position: relative; width: 960px; height: 1200px; overflow: hidden; }

  .header {
    position: absolute; left: 0; top: 0; width: 960px; height: 253px;
    background: var(--deep-teal); text-align: center;
  }
  .job-title {
    position: absolute; left: 0; right: 0; top: 52px;
    font-size: 75px; font-weight: 700; letter-spacing: -0.5px; line-height: 1;
  }
  .subtitle {
    position: absolute; left: 0; right: 0; top: 145px;
    font-size: 46px; font-weight: 700; line-height: 1;
  }

  .photo {
    position: absolute; left: 0; top: 253px; width: 960px; height: 693px;
    background:
      radial-gradient(ellipse at 70% 55%, #e9edf0 0%, transparent 60%),
      linear-gradient(90deg, #3d5a66 0%, #c9d6d9 22%, #f2f4f4 45%, #eef1f2 70%, #e4e9eb 100%);
  }

  .tag, .highlight {
    position: absolute; left: 0; display: flex; align-items: center;
    padding-left: 35px; font-weight: 700; line-height: 1;
  }
  .tag { height: 88px; font-size: 41px; }
  .tag--fulltime {
    top: 269px; width: 253px; background: var(--slate);
    clip-path: polygon(0 0, 100% 0, 91% 100%, 0 100%);
  }
  .tag--parttime {
    top: 371px; width: 226px; background: var(--aqua);
    clip-path: polygon(0 0, 100% 0, 90% 100%, 0 100%);
  }

  .highlight { height: 88px; font-size: 41px; border-radius: 0 44px 44px 0; }
  .highlight--one { top: 529px; width: 802px; background: var(--sun); }
  .highlight--two { top: 658px; width: 264px; background: var(--aqua); }
  .highlight--three { top: 788px; width: 605px; background: var(--slate); }

  .footer {
    position: absolute; left: 0; top: 946px; width: 960px; height: 254px;
    background: var(--brand-teal);
  }
  .location {
    position: absolute; left: 35px; top: 30px;
    font-size: 31px; font-weight: 400;
  }
  .employer {
    position: absolute; left: 0; right: 0; top: 96px; text-align: center;
  }
  .employer-name {
    display: inline-flex; align-items: center; gap: 18px;
    font-size: 84px; font-weight: 300; line-height: 1;
  }
  .employer-dot { width: 34px; height: 34px; border-radius: 50%; background: var(--white); }
  .employer-claim {
    margin-top: 12px; font-size: 15px; font-weight: 700; letter-spacing: 0.5px;
  }
</style>
</head>
<body>
<main class="ad">
  <header class="header">
    <h1 class="job-title">Physiotherapeut (m/w/d)</h1>
    <p class="subtitle">Werde Teil eines wachsenden Teams</p>
  </header>

  <div class="photo" role="img" aria-label="Foto: Physiotherapeutin behandelt das Bein eines älteren Patienten auf einer Liege in einem hellen Praxisraum"></div>

  <div class="tag tag--fulltime">Vollzeit</div>
  <div class="tag tag--parttime">Teilzeit</div>

  <div class="highlight highlight--one">1. Betriebliche Krankenversicherung</div>
  <div class="highlight highlight--two">2. Tretlux</div>
  <div class="highlight highlight--three">3. Gehalt bis zu 4.500 EUR</div>

  <footer class="footer">
    <p class="location">Ort | Hannover</p>
    <div class="employer">
      <div class="employer-name">lusen<span class="employer-dot"></span></div>
      <p class="employer-claim">PHYSIO | FITNESS | WELLNESS</p>
    </div>
  </footer>
</main>
</body>
</html>
```